Business Card Design Project

I need business cards communicate a high end look and cutting edge sophistication,creativity, with a logo branding.
The company name is: Keystone Crafters we specialize in Remodel ing and Design of Resindental and Commercial our company is based in Los Angeles Ca our clients are high end high dollar . The design should communicate the statements above.
Updates
I would like to see both side the business card
Industry/Entity Type
Business
Requirements
Nice to have
- Maybe a design with a faint Blueprint /construction floor plan background, maybe

```html
<!DOCTYPE html>
<html lang="en">
<head>
<meta charset="utf-8">
<title>Keystone Crafters – Business Card</title>
<link href="https://fonts.googleapis.com/css2?family=Nunito:wght@400;600;800&display=swap" rel="stylesheet">
<style>
  :root {
    --page: #e8e5e0;
    --blue: #1a5cc4;
    --blue-deep: #0f46a3;
    --blue-light: #3d7ad6;
    --ink-blue: #1b58b8;
    --band-light: #eef0f2;
    --band-shade: #cfd3d8;
    --band-dark: #2a2d31;
    --white: #ffffff;
  }
  * { box-sizing: border-box; margin: 0; padding: 0; }
  html, body { width: 1200px; height: 880px; overflow: hidden; }
  body {
    background: var(--page);
    font-family: "Nunito", "Helvetica Neue", Arial, sans-serif;
    position: relative;
  }
  .card {
    position: absolute;
    left: 260px;
    width: 680px;
    height: 388px;
    overflow: hidden;
    border-radius: 4px;
    background: radial-gradient(ellipse at 40% 40%, var(--blue-light) 0%, var(--blue) 45%, var(--blue-deep) 100%);
    box-shadow: 0 6px 18px rgba(0,0,0,0.18);
  }
  .card--front { top: 30px; }
  .card--back { top: 462px; }

  /* Front */
  .brand-name {
    position: absolute;
    left: 64px;
    top: 78px;
    width: 560px;
    color: var(--white);
    font-weight: 800;
    font-size: 76px;
    line-height: 1.02;
    letter-spacing: 0.02em;
    text-transform: uppercase;
  }
  .tagline-band {
    position: absolute;
    left: 0; right: 0; bottom: 0;
    height: 50px;
    background: linear-gradient(180deg, var(--band-light), var(--band-shade));
    display: flex;
    align-items: center;
    justify-content: center;
  }
  .tagline {
    color: var(--ink-blue);
    font-weight: 600;
    font-size: 20px;
    letter-spacing: 0.42em;
    text-transform: uppercase;
  }

  /* Back */
  .name-band {
    position: absolute;
    top: 34px; left: 150px; right: 0;
    height: 56px;
    background: linear-gradient(180deg, var(--white), var(--band-light));
    clip-path: polygon(34px 0, 100% 0, 100% 100%, 0 100%);
    display: flex;
    align-items: center;
    padding-left: 56px;
  }
  .person-name {
    color: var(--ink-blue);
    font-weight: 800;
    font-size: 36px;
  }
  .contact-band {
    position: absolute;
    top: 90px; left: 150px; right: 0;
    height: 36px;
    background: var(--band-dark);
    display: flex;
    align-items: center;
    padding-left: 56px;
    color: var(--white);
    font-size: 19px;
    font-weight: 400;
    gap: 12px;
  }
  .contact-divider { opacity: 0.8; }
  .address {
    position: absolute;
    left: 40px;
    top: 156px;
    color: var(--white);
    font-size: 23px;
    line-height: 1.3;
    font-weight: 400;
    font-style: normal;
  }
  .license {
    display: block;
    margin-top: 4px;
    font-size: 12px;
    opacity: 0.9;
  }
  .building-art {
    position: absolute;
    right: 0;
    bottom: 0;
    width: 360px;
    height: 262px;
    background: linear-gradient(160deg, rgba(255,255,255,0.05) 0%, rgba(200,220,255,0.28) 55%, rgba(255,255,255,0.12) 100%);
  }
</style>
</head>
<body>
  <section class="card card--front" aria-label="Business card front">
    <h1 class="brand-name">Keystone Crafters</h1>
    <div class="tagline-band">
      <p class="tagline">Remodeling &amp; Design</p>
    </div>
  </section>

  <section class="card card--back" aria-label="Business card back">
    <div class="building-art" role="img" aria-label="White line drawing of a modern multi-storey house"></div>
    <div class="name-band">
      <h2 class="person-name">Morgan Ellery</h2>
    </div>
    <div class="contact-band">
      <span class="contact-phone">213-555-0148</span>
      <span class="contact-divider">|</span>
      <span class="contact-email">morgan@keystonecrafters.net</span>
    </div>
    <address class="address">
      4820 Larchmont Ave<br>
      Suite# 900<br>
      Los Angeles, CA 90004
      <span class="license">License 507316</span>
    </address>
  </section>
</body>
</html>
```